Digital Signage Mockup template

I would like to have some mock ups for digital signage templates(content on screens) - deliverable should be psd file + png export; it is to promote a digital signage business and can be fictive examples about fictive company as well as of a real example; use recent design trends (material design or more recent)
- corporate - welcome board (weather, news, anniversary wishes, visiting guests, ticker text) : 3 variations + landscape and portrait
- corporate : meeting room reservation screen - landscape only ; 2 variations
see example as inspiration :
https://www.lumavexo.com/sites/default/files/reception%20landscape.png
https://www.brightquillo.com/blog/corporate-digital-signage/
Other font styles liked:
- Nero Sans

```html
<!DOCTYPE html>
<html lang="en">
<head>
<meta charset="utf-8">
<title>Digital Signage Screens – Norvale</title>
<link rel="stylesheet" href="https://fonts.googleapis.com/css2?family=Lato:wght@100;300;400;700&family=Raleway:wght@500;600;700;800;900&display=swap">
<style>
  :root{
    --page:#ffffff;
    --white:#ffffff;
    --welcome-top:#3f7dbd;
    --welcome-bottom:#1d4c92;
    --teal-photo-a:#2aa996;
    --teal-photo-b:#139683;
    --royal:#0652a6;
    --mic-a:#7a1e44;
    --mic-b:#3e0d2a;
    --mic-warm:#a8553f;
    --teal:#00a98f;
    --news-box:#0a51a8;
  }
  *{box-sizing:border-box;margin:0;padding:0}
  html,body{width:1200px;height:1200px;overflow:hidden;background:var(--page)}
  body{position:relative;font-family:"Raleway",sans-serif;color:var(--white)}

  .screen{position:absolute;overflow:hidden}
  .brand{position:absolute;display:flex;align-items:center;gap:10px;transform:translateX(-50%);white-space:nowrap}
  .brand__dot{width:24px;height:24px;border-radius:50%;background:var(--white)}
  .brand__name{font-family:"Raleway",sans-serif;font-weight:800;font-size:26px;letter-spacing:1px;color:var(--white)}

  /* Welcome screen */
  .welcome{left:262px;top:21px;width:676px;height:379px}
  .welcome__photo{position:absolute;inset:0;background:linear-gradient(175deg,var(--welcome-top) 0%,#3670b2 45%,var(--welcome-bottom) 100%)}
  .welcome__title{position:absolute;left:0;right:0;top:62px;text-align:center;font-weight:900;font-size:80px;letter-spacing:-1px;line-height:1}
  .welcome__to{position:absolute;left:178px;width:320px;top:157px;display:flex;align-items:center;gap:14px;font-weight:800;font-size:18px}
  .welcome__to::before,.welcome__to::after{content:"";flex:1;height:1.5px;background:var(--white)}
  .welcome .brand{left:338px;top:254px}

  /* Weather screen */
  .weather{left:263px;top:412px;width:674px;height:379px}
  .weather__photo{position:absolute;left:0;top:0;width:391px;height:100%;background:radial-gradient(ellipse at 45% 35%,#3fb49a 0%,var(--teal-photo-a) 45%,var(--teal-photo-b) 100%)}
  .weather__sun{position:absolute;left:43px;top:26px;width:70px;height:70px}
  .weather__temp{position:absolute;left:40px;top:116px;font-family:"Lato",sans-serif;font-weight:100;font-size:96px;line-height:1}
  .weather__time{position:absolute;left:43px;top:288px;font-family:"Lato",sans-serif;font-size:40px;line-height:1}
  .weather__time b{font-weight:700}
  .weather__time span{font-weight:300}
  .weather__date{position:absolute;left:43px;top:330px;font-family:"Lato",sans-serif;font-weight:700;font-size:19px}
  .weather__side{position:absolute;left:391px;top:0;width:283px;height:100%;background:var(--royal)}
  .weather__icon{position:absolute;left:24px;width:54px;height:54px}
  .weather__value{position:absolute;right:24px;font-family:"Lato",sans-serif;font-weight:700;font-size:38px;line-height:1}
  .weather__value small{font-size:24px;margin-left:6px}
  .weather__side .brand{left:142px;top:296px}

  /* News screen */
  .news{left:266px;top:804px;width:669px;height:375px;background:var(--teal)}
  .news__photo{position:absolute;left:0;top:0;width:302px;height:100%;background:radial-gradient(ellipse at 48% 48%,var(--mic-warm) 0%,#8a2e45 28%,var(--mic-a) 55%,var(--mic-b) 100%)}
  .news__photo + .brand{left:154px;top:304px}
  .news__headline{position:absolute;left:248px;top:20px;width:397px;height:116px;background:var(--news-box);box-shadow:0 6px 14px rgba(0,0,0,.28);padding:22px 20px 0}
  .news__kicker{font-weight:700;font-size:30px;line-height:34px;letter-spacing:-.2px}
  .news__title{font-weight:500;font-size:30px;line-height:34px}
  .news__body{position:absolute;left:322px;top:160px;width:330px;font-weight:500;font-size:14.5px;line-height:18px}
  .news__body p + p{margin-top:18px}
</style>
</head>
<body>

<section class="screen welcome">
  <div class="welcome__photo" role="img" aria-label="Misty pine forest under a blue tint"></div>
  <h1 class="welcome__title">WELCOME</h1>
  <div class="welcome__to">TO</div>
  <div class="brand"><span class="brand__dot"></span><span class="brand__name">NORVALE</span></div>
</section>

<section class="screen weather">
  <div class="weather__photo" role="img" aria-label="Snowy mountain peak under a teal tint"></div>
  <svg class="weather__sun" viewBox="0 0 70 70" fill="none" stroke="#fff" stroke-width="4" stroke-linecap="round">
    <circle cx="35" cy="35" r="14"/>
    <line x1="35" y1="3" x2="35" y2="11"/><line x1="35" y1="59" x2="35" y2="67"/>
    <line x1="3" y1="35" x2="11" y2="35"/><line x1="59" y1="35" x2="67" y2="35"/>
    <line x1="12" y1="12" x2="18" y2="18"/><line x1="52" y1="52" x2="58" y2="58"/>
    <line x1="58" y1="12" x2="52" y2="18"/><line x1="18" y1="52" x2="12" y2="58"/>
  </svg>
  <div class="weather__temp">27°C</div>
  <div class="weather__time"><b>11:50</b> <span>SUNDAY</span></div>
  <div class="weather__date">15 MARCH, 2018</div>

  <div class="weather__side">
    <svg class="weather__icon" style="top:26px" viewBox="0 0 54 54" fill="none" stroke="#fff" stroke-width="3" stroke-linecap="round" stroke-linejoin="round">
      <path d="M12 32 h32 a8 8 0 0 0 0-16 a13 13 0 0 0-25-3 a9 9 0 0 0-7 19z"/>
      <line x1="14" y1="40" x2="10" y2="48"/><line x1="22" y1="40" x2="18" y2="48"/>
      <line x1="30" y1="40" x2="26" y2="48"/><line x1="38" y1="40" x2="34" y2="48"/>
      <line x1="46" y1="40" x2="42" y2="48"/>
    </svg>
    <div class="weather__value" style="top:36px">2%</div>

    <svg class="weather__icon" style="top:122px" viewBox="0 0 54 54" fill="none" stroke="#fff" stroke-width="3" stroke-linecap="round">
      <path d="M4 18 h28 a6 6 0 1 0-6-6"/>
      <path d="M2 27 h40 a7 7 0 1 1-7 7"/>
      <path d="M8 36 h18 a6 6 0 1 1-6 6"/>
    </svg>
    <div class="weather__value" style="top:130px">8<small>km/h</small></div>

    <div class="brand"><span class="brand__dot"></span><span class="brand__name">NORVALE</span></div>
  </div>
</section>

<section class="screen news">
  <div class="news__photo" role="img" aria-label="Studio condenser microphone in warm purple light"></div>
  <div class="brand"><span class="brand__dot"></span><span class="brand__name">NORVALE</span></div>
  <div class="news__headline">
    <div class="news__kicker">NEWS OF THE DAY</div>
    <div class="news__title">Lorem Ipsum is simply</div>
  </div>
  <div class="news__body">
    <p>Lorem Ipsum is simply dummy text of the printing and typesetting industry. Lorem Ips has been the industry's standard dummy text ever</p>
    <p>Lorem Ipsum has been the industry's standard dummy text ever</p>
  </div>
</section>

</body>
</html>
```